Postcard Design for Birchfield Medical Center Integrated Medicine

We need a postcard that we will be able to hand out at events that gives an overview of what we do at Birchfield Medical Center. Birchfield Medical Center, located in Encinitas, California, is an integrated medical center using functional medicine to prevent and reverse chronic diseases. We would also like to highly emphasize that we take Medicare and PPO insurance for these services and if patients have any questions to contact the front desk.

The attached screenshots are elementary versions of what we hope our postcard will have.

THIS IS NOT INTENDED TO BE MAILED SO AN ADDRESS SPACE IS NOT NEEDED
ALSO, WE WOULD LIKE TO HAVE THIS SIZE 6X4

Birchfieldmedcenter.net is our website if you would need any further information about the company.

```html
<!DOCTYPE html>
<html lang="en">
<head>
<meta charset="utf-8">
<title>Birchfield Medical Center – Event Postcard</title>
<link href="https://fonts.googleapis.com/css2?family=Questrial&display=swap" rel="stylesheet">
<style>
  :root{
    --page:#e8ebee;
    --band:#5eaed1;
    --wave:#d5ebf5;
    --wave-soft:#eaf5fa;
    --accent:#4aa2c8;
    --ink:#5c6166;
    --alert:#de2a2f;
    --white:#ffffff;
  }
  *{margin:0;padding:0;box-sizing:border-box}
  html,body{width:1200px;height:1000px;overflow:hidden;background:var(--page)}
  body{font-family:"Questrial",sans-serif;color:var(--ink);position:relative}
  .postcard{position:absolute;left:255px;width:690px;height:460px;background:var(--white);
    box-shadow:0 6px 18px rgba(0,0,0,.18);overflow:hidden}
  .postcard--conditions{top:25px}
  .postcard--intro{top:515px}
  .postcard__art{position:absolute;inset:0;width:690px;height:460px}
  .band-text{position:absolute;bottom:0;left:0;right:0;height:48px;display:flex;align-items:center;
    justify-content:space-between;padding:0 28px;color:var(--white);font-size:19px;letter-spacing:.3px}
  .band-text--end{justify-content:flex-end}

  .brand{position:absolute;display:flex;align-items:center;gap:8px;color:var(--accent);white-space:nowrap}
  .brand__dot{width:30px;height:30px;border-radius:50%;background:var(--accent);flex:none}
  .brand__name{font-size:26px;line-height:1}
  .brand__sub{display:block;font-size:9px;letter-spacing:1px;text-transform:uppercase;margin-top:3px}

  .conditions__title{position:absolute;left:30px;top:30px;color:var(--accent);font-size:19px;
    line-height:1.1;text-transform:uppercase;letter-spacing:.5px}
  .conditions__list{position:absolute;left:30px;top:86px;width:320px;columns:2;column-gap:16px;
    list-style:none;font-size:10.4px;line-height:12.6px}
  .conditions__list li{break-inside:avoid}
  .insurance-note{position:absolute;left:30px;top:358px;color:var(--alert);font-size:12.5px;line-height:15px}

  .intro__copy{position:absolute;left:300px;top:252px;width:380px}
  .intro__headline{color:var(--accent);font-size:19px;font-weight:400;margin-bottom:10px;white-space:nowrap}
  .intro__body{font-size:10.5px;line-height:15px;color:var(--ink)}
  .intro__doctor{margin-top:14px;color:var(--accent);font-size:13px}
</style>
</head>
<body>

<section class="postcard postcard--conditions" aria-label="Postcard back – conditions we treat">
  <svg class="postcard__art" viewBox="0 0 690 460">
    <defs>
      <linearGradient id="resortTones" x1="0" y1="0" x2="1" y2="1">
        <stop offset="0" stop-color="#7fa8c4"/>
        <stop offset=".45" stop-color="#8a9a6a"/>
        <stop offset="1" stop-color="#c9c2b2"/>
      </linearGradient>
    </defs>
    <path role="img" aria-label="Photo: oceanfront resort terrace with palm trees and lounge seating"
      d="M360,0 L690,0 L690,240 C600,255 500,240 450,190 C400,140 380,70 360,0 Z" fill="url(#resortTones)"/>
    <path d="M340,0 C360,90 400,170 450,215 C520,262 600,272 690,262 L690,280 C590,292 500,278 440,228 C380,178 345,100 325,0 Z" fill="var(--wave)"/>
    <path d="M0,300 C180,250 320,330 470,330 C560,330 630,310 690,300 L690,412 L0,412 Z" fill="var(--wave-soft)"/>
    <path d="M0,330 C200,290 360,360 690,330" stroke="var(--wave)" stroke-width="3" fill="none"/>
    <rect x="0" y="404" width="690" height="8" fill="var(--wave)"/>
    <rect x="0" y="412" width="690" height="48" fill="var(--band)"/>
  </svg>

  <h2 class="conditions__title">Some of the conditions<br>we treat:</h2>
  <ul class="conditions__list">
    <li>Acne</li>
    <li>Alzheimer's disease and Dementia</li>
    <li>Arthritis</li>
    <li>Asthma</li>
    <li>Autism Spectrum Disorder, ADD/ADHD</li>
    <li>Autoimmune Diseases</li>
    <li>Cancer Prevention</li>
    <li>Chronic Fatigue</li>
    <li>Chronic Sinusitis</li>
    <li>Depression and Anxiety</li>
    <li>Detoxification and Healing</li>
    <li>Diabetes</li>
    <li>Digestive Disorders (IBD, IBS, GERD/Reflux)</li>
    <li>Eczema/Psoriasis</li>
    <li>Elevated Cholesterol</li>
    <li>Environmental and Food Allergies</li>
    <li>Fatigue</li>
    <li>Female Disorders (PMS, Endometriosis, Menopause, Infertility, PCOS)</li>
    <li>Fibromyalgia</li>
    <li>Healthy Aging</li>
    <li>Healthy Weight and Metabolism</li>
    <li>Heart Health</li>
    <li>Hormone Balance</li>
    <li>Interstitial Cystitis</li>
    <li>Memory and Mental Clarity</li>
    <li>Metabolic Syndrome, Pre-Diabetes, Insulin Resistance</li>
    <li>Migraines and Headaches</li>
    <li>MS (Multiple Sclerosis)</li>
    <li>Osteoporosis</li>
    <li>Parkinson's disease</li>
    <li>Restless Leg Syndrome</li>
    <li>Sleep Disorders</li>
    <li>Thyroid and Adrenal Disorders</li>
    <li>And many more</li>
  </ul>

  <p class="insurance-note">We Accept all Medicare and PPO Insurance<br>Please contact the front desk for more information</p>

  <div class="brand" style="left:440px;top:300px">
    <span class="brand__dot"></span>
    <span class="brand__name">Birchfield<span class="brand__sub">Medical Center · Integrated Medicine</span></span>
  </div>

  <div class="band-text band-text--end"><span>418 Seabright Avenue #200, Larkspur Bay, CA 90871</span></div>
</section>

<section class="postcard postcard--intro" aria-label="Postcard front – introduction">
  <svg class="postcard__art" viewBox="0 0 690 460">
    <defs>
      <linearGradient id="seaTones" x1="0" y1="0" x2="1" y2="1">
        <stop offset="0" stop-color="#3f8f95"/>
        <stop offset=".5" stop-color="#6fb3ad"/>
        <stop offset="1" stop-color="#a9d3cf"/>
      </linearGradient>
    </defs>
    <rect role="img" aria-label="Photo: swimmer and dolphin underwater in clear tropical sea"
      x="0" y="0" width="690" height="412" fill="url(#seaTones)"/>
    <path d="M0,290 C170,290 330,220 470,150 C560,105 630,80 690,75 L690,412 L0,412 Z" fill="var(--wave)"/>
    <path d="M0,310 C180,305 340,240 480,170 C570,125 635,100 690,96 L690,412 L0,412 Z" fill="var(--white)"/>
    <path d="M300,236 C420,210 540,175 690,140" stroke="var(--wave)" stroke-width="2" fill="none"/>
    <path d="M300,392 C430,380 560,340 690,300" stroke="var(--wave-soft)" stroke-width="6" fill="none"/>
    <rect x="0" y="404" width="690" height="8" fill="var(--wave)"/>
    <rect x="0" y="412" width="690" height="48" fill="var(--band)"/>
  </svg>

  <div class="brand" style="left:28px;top:338px">
    <span class="brand__dot"></span>
    <span class="brand__name">Birchfield<span class="brand__sub">Medical Center · Integrated Medicine</span></span>
  </div>

  <div class="intro__copy">
    <h1 class="intro__headline">Healing the Whole Person: Mind, Body, Spirit</h1>
    <p class="intro__body">Holistic medicine called lifestyle functional medicine.<br>
      Treating root causes not symptoms using a whole system approach,<br>
      forestalling chronic disease and creating optimal health and vitality.</p>
    <p class="intro__doctor">Dr. Marisa Holloway, M.D. ABAARM</p>
  </div>

  <div class="band-text"><span>www.birchfieldmedcenter.net</span><span>760-555-0142</span></div>
</section>

</body>
</html>
```